Happy Birthday Postcard for law firm for existing clients

Need a postcard that will go out to our current clients on their birthdays. Prefer to have our logo incorporated as part of the design so it reminds them about our business. The back needs to say "Happy Birthday from the team at Dunmore Law Firm."

We are a law firm that services local clients. Needs to be mailed so the backside right half needs to be left blank except the return address (in NEEDS below) so it can be mailed with a mailing label.

Target Market(s)

existing customers, varying age range and demographic profile

Industry/Entity Type

Legal

Font styles to use
Sans Serif
Script

Colors

Designer to choose colors to be used in the design.

Requirements
Must have
• Our logo preferrably on the front (can be modified or added to so it fits a birthday message. And needs to be mailed so the back right side needs to be left open for address labels. The firms return address is
• Dunmore Law Firm
• 4718 W Pebblecrest Ave
• Springfield, MO 65917
• Needs to have the text included in the project description on the back, or some close iteration of it if space is limited.
Nice to have
• Some illustration or graphic on the front with the logo that shows it is a birthday postcard

```html
<!DOCTYPE html>
<html lang="en">
<head>
<meta charset="utf-8">
<title>Dunmore Law Firm – Birthday Postcard</title>
<link rel="stylesheet" href="https://fonts.googleapis.com/css2?family=Great+Vibes&family=Montserrat:wght@300&family=Open+Sans:ital,wght@0,400;0,700;1,400&family=Roboto+Condensed:wght@700&display=swap">
<style>
  :root {
    --page-bg: #eceae6;
    --card-white: #ffffff;
    --photo-teal: #a9dfe0;
    --photo-teal-light: #c8ecea;
    --photo-pink: #d84d86;
    --script-pink: #c73d77;
    --brand-grey: #5d6770;
    --stripe-cyan: #c6f1f5;
    --stripe-blue: #a8cbe6;
    --ink: #1a1a1a;
    --stamp-line: #a7a7a7;
  }
  * { box-sizing: border-box; margin: 0; padding: 0; }
  html, body { width: 1200px; height: 528px; overflow: hidden; background: var(--page-bg); }
  .canvas { position: relative; width: 1200px; height: 528px; }

  .card { position: absolute; top: 58px; height: 416px; overflow: hidden; }

  /* Front */
  .card-front { left: 50px; width: 538px; }
  .front-photo {
    position: absolute; inset: 0;
    background:
      radial-gradient(ellipse 120px 150px at 430px 330px, rgba(216,77,134,0.55), transparent 70%),
      radial-gradient(ellipse 180px 160px at 370px 110px, rgba(255,255,255,0.55), transparent 70%),
      linear-gradient(180deg, var(--photo-teal) 0%, var(--photo-teal-light) 100%);
  }
  .front-greeting {
    position: absolute; left: 62px; top: 62px;
    font-family: "Great Vibes", cursive;
    color: var(--script-pink);
    font-size: 78px; line-height: 72px;
  }
  .front-greeting span { display: block; }
  .front-greeting .line-2 { margin-left: 10px; }
  .front-brand {
    position: absolute; left: 70px; top: 314px;
    font-family: "Montserrat", sans-serif; font-weight: 300;
    font-size: 25px; letter-spacing: 1px; color: var(--brand-grey);
  }

  /* Back */
  .card-back { left: 624px; width: 537px; background: var(--card-white); }
  .back-greeting-panel {
    position: absolute; left: 0; top: 0; width: 270px; height: 100%;
    background: repeating-linear-gradient(180deg,
      var(--stripe-blue) 0 28px, var(--stripe-cyan) 28px 56px);
  }
  .back-greeting-panel::after {
    content: ""; position: absolute; inset: 0;
    background: linear-gradient(90deg, rgba(255,255,255,0.15) 0%, rgba(255,255,255,0) 40%, rgba(255,255,255,0) 80%, #fff 100%);
  }
  .back-message {
    position: absolute; left: 0; width: 270px; top: 140px;
    text-align: center; z-index: 1; color: var(--ink);
  }
  .back-message .headline {
    font-family: "Roboto Condensed", sans-serif; font-weight: 700;
    font-size: 38px; line-height: 40px; display: block;
  }
  .back-message .from-line {
    font-family: "Open Sans", sans-serif; font-style: italic;
    font-size: 15px; display: block; margin-top: 4px;
  }
  .back-message .firm-name {
    font-family: "Open Sans", sans-serif; font-weight: 700;
    font-size: 21px; display: block;
  }

  .return-address { position: absolute; left: 301px; top: 52px; }
  .return-address .brand {
    font-family: "Montserrat", sans-serif; font-weight: 300;
    font-size: 17px; letter-spacing: 0.5px; color: var(--brand-grey);
    margin-bottom: 12px;
  }
  .return-address address {
    font-style: normal; font-family: "Roboto Condensed", sans-serif; font-weight: 700;
    font-size: 10.5px; line-height: 16px; color: var(--ink);
  }
  .stamp-box { position: absolute; left: 445px; top: 13px; }
</style>
</head>
<body>
<main class="canvas">

  <section class="card card-front" aria-label="Postcard front">
    <div class="front-photo" role="img" aria-label="Photo of a pink frosted cupcake with rainbow sprinkles and a lit sparkler on a soft teal background"></div>
    <h1 class="front-greeting"><span class="line-1">Happy</span><span class="line-2">Birthday!</span></h1>
    <p class="front-brand">DUNMORE LAW</p>
  </section>

  <section class="card card-back" aria-label="Postcard back">
    <div class="back-greeting-panel"></div>
    <p class="back-message">
      <span class="headline">Happy</span>
      <span class="headline">Birthday</span>
      <span class="from-line">from the team at</span>
      <span class="firm-name">Dunmore Law Firm</span>
    </p>

    <div class="return-address">
      <p class="brand">DUNMORE LAW</p>
      <address>4718 W Pebblecrest Ave<br>Springfield, MO 65917</address>
    </div>

    <svg class="stamp-box" width="68" height="67" viewBox="0 0 68 67" aria-label="Stamp placement">
      <rect x="1" y="1" width="66" height="65" fill="none" stroke="var(--stamp-line)" stroke-width="2" stroke-dasharray="6 4"/>
    </svg>
  </section>

</main>
</body>
</html>
```